Vantora88 - a Political Plebescite app.

There is a current app in the App Store (worldwide) and Play Store (worldwide) called yourBallot (with an owl logo). The UX needs to be redesigned to make it more visually pleasing.

The requirement is to build a UX that is suitable for both iOS and Android - i.e. consistent look for both platforms. The design is to span the variety of sizes available from smart devices - phones and tablets. The layout as it stands is portrait only, and a secondary design to encompass landscape is wanted.

You would need to download the app to get a feel for all the functionality - there are 3 visible forms (currently) and a hidden form, that will be used in the near future - this hidden form will look similar to the main (first) form.

To get full functionality you need to do the following:
Go to the Options page
Toggle the top slide
Click on UNREGISTERED
Select a state/territory

I know this is a bit non-intuitive - in the "real" product these steps are automated - but for this release the user gets to choose.

Once this is done - the other button(s) appear in the top left of the screen - and data is available to be displayed.

The current forms are included in this brief. The Options screen will ultimately not be showing all the current data, only the lower slider (or other indicator) and the associated version and copyright notices. The hidden screen is much like the main screen - showing the name of the bill and information pertaining to that bill - there needs to be a button (or action site) to toggle between the main and this hidden screen.

Target Market(s)

All eligable voters (currently in Australia)

Industry/Entity Type

Political

Requirements
Should not have
• Do not present to me my own/existing design with the only change being colours and label layout.

```html
<!DOCTYPE html>
<html lang="en">
<head>
<meta charset="utf-8">
<title>Settings</title>
<link rel="stylesheet" href="https://fonts.googleapis.com/css2?family=Inter:wght@400;600&display=swap">
<style>
  :root {
    --page-bg: #ffffff;
    --bar-bg: #f7f7f8;
    --group-bg: #efeff4;
    --cell-bg: #ffffff;
    --separator: #c8c7cc;
    --text: #000000;
    --detail: #8e8e93;
    --chevron: #c7c7cc;
    --accent: #007aff;
    --knob: #ffffff;
  }
  * { box-sizing: border-box; margin: 0; padding: 0; }
  html, body {
    width: 1200px; height: 1200px; overflow: hidden;
    background: var(--page-bg);
    font-family: "Inter", "Helvetica Neue", Arial, sans-serif;
    color: var(--text);
  }
  .screen {
    position: absolute; left: 288px; top: 41px;
    width: 624px; height: 1117px;
    background: var(--group-bg);
    overflow: hidden;
  }
  .status-bar {
    height: 31px; background: var(--bar-bg);
    display: flex; align-items: center; justify-content: space-between;
    padding: 0 12px 0 8px; font-size: 18px;
  }
  .status-bar .time { font-weight: 600; position: absolute; left: 0; right: 0; text-align: center; top: 5px; }
  .status-left, .status-right { display: flex; align-items: center; gap: 6px; }
  .nav-bar {
    height: 107px; background: var(--bar-bg);
    border-bottom: 1px solid var(--separator);
    position: relative;
  }
  .nav-title {
    position: absolute; left: 0; right: 0; top: 47px;
    text-align: center; font-weight: 600; font-size: 27px;
  }
  .nav-back {
    position: absolute; left: 14px; top: 52px;
    display: flex; align-items: center; gap: 4px;
    color: var(--accent); font-size: 24px;
  }
  .group {
    background: var(--cell-bg);
    border-top: 1px solid var(--separator);
    border-bottom: 1px solid var(--separator);
  }
  .group.first { margin-top: 38px; }
  .group.second { margin-top: 40px; }
  .cell {
    position: relative; display: flex; align-items: center;
    padding: 0 34px 0 28px; font-size: 27px;
  }
  .cell + .cell::before {
    content: ""; position: absolute; left: 25px; right: 0; top: 0;
    border-top: 1px solid var(--separator);
  }
  .group.first .cell { height: 89px; }
  .group.second .cell { height: 75px; }
  .cell-label { flex: 1; }
  .cell-detail { color: var(--detail); margin-right: 14px; }
  .toggle {
    width: 94px; height: 50px; border-radius: 25px;
    background: var(--accent); position: relative;
  }
  .toggle::after {
    content: ""; position: absolute; right: 2px; top: 2px;
    width: 46px; height: 46px; border-radius: 50%;
    background: var(--knob); box-shadow: 0 2px 4px rgba(0,0,0,.25);
  }
</style>
</head>
<body>
<main class="screen">
  <div class="status-bar">
    <div class="status-left">
      <svg width="58" height="10" viewBox="0 0 58 10" fill="#000"><circle cx="5" cy="5" r="4.5"/><circle cx="17" cy="5" r="4.5"/><circle cx="29" cy="5" r="4.5"/><circle cx="41" cy="5" r="4.5"/><circle cx="53" cy="5" r="4.5"/></svg>
      <svg width="20" height="15" viewBox="0 0 20 15" fill="none" stroke="#000" stroke-width="2.2" stroke-linecap="round"><path d="M2 5a11 11 0 0 1 16 0"/><path d="M5 8.5a6.5 6.5 0 0 1 10 0"/><circle cx="10" cy="12.5" r="1.6" fill="#000" stroke="none"/></svg>
    </div>
    <span class="time">9:41 AM</span>
    <div class="status-right">
      <span>100%</span>
      <svg width="42" height="16" viewBox="0 0 42 16"><rect x="0.5" y="0.5" width="38" height="15" rx="2.5" fill="none" stroke="#000"/><rect x="2.5" y="2.5" width="34" height="11" rx="1" fill="#000"/><rect x="39.5" y="5" width="2.5" height="6" rx="1" fill="#000"/></svg>
    </div>
  </div>
  <header class="nav-bar">
    <div class="nav-back">
      <svg width="14" height="24" viewBox="0 0 14 24" fill="none" stroke="currentColor" stroke-width="3" stroke-linecap="round" stroke-linejoin="round"><path d="M12 2 2 12l10 10"/></svg>
      <span>Back</span>
    </div>
    <h1 class="nav-title">Settings</h1>
  </header>

  <section class="group first">
    <div class="cell"><span class="cell-label">Show Legislative Assembly</span><span class="toggle"></span></div>
    <div class="cell"><span class="cell-label">Hide Bills after Opinion</span><span class="toggle"></span></div>
  </section>

  <section class="group second">
    <div class="cell"><span class="cell-label">Help</span>
      <svg class="chevron" width="11" height="20" viewBox="0 0 11 20" fill="none" stroke="var(--chevron)" stroke-width="2.5" stroke-linecap="round" stroke-linejoin="round"><path d="M2 2l7 8-7 8"/></svg></div>
    <div class="cell"><span class="cell-label">FAQs</span>
      <svg class="chevron" width="11" height="20" viewBox="0 0 11 20" fill="none" stroke="var(--chevron)" stroke-width="2.5" stroke-linecap="round" stroke-linejoin="round"><path d="M2 2l7 8-7 8"/></svg></div>
    <div class="cell"><span class="cell-label">Contact Us</span>
      <svg class="chevron" width="11" height="20" viewBox="0 0 11 20" fill="none" stroke="var(--chevron)" stroke-width="2.5" stroke-linecap="round" stroke-linejoin="round"><path d="M2 2l7 8-7 8"/></svg></div>
    <div class="cell"><span class="cell-label">About</span><span class="cell-detail">v 0.752</span>
      <svg class="chevron" width="11" height="20" viewBox="0 0 11 20" fill="none" stroke="var(--chevron)" stroke-width="2.5" stroke-linecap="round" stroke-linejoin="round"><path d="M2 2l7 8-7 8"/></svg></div>
  </section>
</main>
</body>
</html>
```